Real Estate Listing Signs for standard Yard arms

I need real estate listing signs done, for the standard sized sign to be hung beneath a white yard arm. To match existing logo. Information to be included:
-Logo
-Business name
-Phone number
-Marden Fosk Tundra Circle & Marden Fosk Realty logos (smaller print)

Colors to be Red and anywhere in the gray scale between black and white, or a combination of those.

Target Market(s)

Drive by visuals

Industry/Entity Type

Real Estate Agent

Colors

Designer to choose only greyscale colors for use in the design.

Requirements
Must have
• My Logo and business name in same/similar font to whats provided, the MF tundra circle logo (small on bottom or corner somewhere), My phone number, and a decent amount of red coloration on the sign.

```html
<!DOCTYPE html>
<html lang="en">
<head>
<meta charset="utf-8">
<title>Morgan Halvik – Listing Sign</title>
<link rel="stylesheet" href="https://fonts.googleapis.com/css2?family=Oswald:wght@500;700&display=swap">
<style>
  :root {
    --sign-red: #d8261c;
    --sign-black: #1c1a1a;
    --band-gray: #7a7878;
    --frame: #111;
    --white: #ffffff;
    --ink: #141414;
    --backdrop: #e9e9e7;
  }
  * { margin: 0; padding: 0; box-sizing: border-box; }
  html, body { width: 1200px; height: 1200px; overflow: hidden; }
  body {
    background: var(--backdrop);
    font-family: "Oswald", sans-serif;
    position: relative;
  }
  .sign {
    position: absolute;
    left: 50px; top: 120px;
    width: 1100px; height: 960px;
    background: var(--frame);
    padding: 14px;
    border-radius: 6px;
  }
  .sign-face {
    position: relative;
    width: 100%; height: 100%;
    overflow: hidden;
    background: var(--sign-red);
  }
  .sign-bands { position: absolute; inset: 0; width: 100%; height: 100%; }
  .brand-box {
    position: absolute;
    left: 30px; top: 40px;
    width: 270px; height: 480px;
    background: var(--white);
    display: flex; flex-direction: column;
    align-items: center; justify-content: center;
    gap: 36px;
  }
  .brand-square {
    width: 120px; height: 120px;
    background: var(--sign-red);
  }
  .brand-name {
    color: var(--ink);
    font-weight: 700;
    font-size: 64px;
    line-height: 1.1;
    text-align: center;
    text-transform: uppercase;
  }
  .agent-name {
    position: absolute;
    left: 340px; top: 40px;
    width: 700px;
    color: var(--white);
    font-weight: 700;
    font-size: 188px;
    line-height: 1.08;
    text-transform: uppercase;
    letter-spacing: 0;
    white-space: nowrap;
  }
  .contact {
    position: absolute;
    left: 0; right: 0; top: 585px;
    text-align: center;
    color: var(--white);
    font-weight: 700;
  }
  .contact-phone { font-size: 150px; line-height: 1.05; letter-spacing: 1px; }
  .contact-email { font-size: 58px; line-height: 1.1; font-weight: 500; }
  .office-badge {
    position: absolute;
    left: 50%; bottom: 0;
    transform: translateX(-50%);
    width: 300px; height: 100px;
    background: var(--white);
    border-radius: 10px 10px 0 0;
    display: flex; flex-direction: column;
    align-items: center; justify-content: center;
    color: var(--ink);
    font-weight: 500;
    text-transform: uppercase;
    line-height: 1.1;
  }
  .office-badge .office-name { font-size: 34px; }
  .office-badge .office-parent { font-size: 17px; letter-spacing: 1px; }
  .office-disclaimer {
    position: absolute;
    right: 24px; bottom: 40px;
    width: 190px;
    color: var(--white);
    font-size: 16px;
    font-weight: 500;
    line-height: 1.3;
    text-align: left;
  }
</style>
</head>
<body>
  <div class="sign">
    <div class="sign-face">
      <svg class="sign-bands" viewBox="0 0 1072 932" preserveAspectRatio="none" aria-hidden="true">
        <path d="M0,580 Q536,470 1072,520 L1072,932 L0,932 Z" fill="var(--band-gray)"/>
        <path d="M0,602 Q536,492 1072,544 L1072,932 L0,932 Z" fill="var(--sign-black)"/>
      </svg>

      <div class="brand-box">
        <div class="brand-square"></div>
        <div class="brand-name">Halvik<br>Realty</div>
      </div>

      <h1 class="agent-name">Morgan<br>Halvik</h1>

      <div class="contact">
        <p class="contact-phone">907-555-0148</p>
        <p class="contact-email">mhalvik@mailbox.com</p>
      </div>

      <div class="office-badge">
        <span class="office-name">MF Tundra Circle</span>
        <span class="office-parent">Marden Fosk Realty</span>
      </div>

      <p class="office-disclaimer">Each Office Independently Owned and Operated</p>
    </div>
  </div>
</body>
</html>
```